Business card for mobile auto detailing company
Brisk auto detailing - Business card
Business card for mobile auto detailing company - Automotive
Creative Brief
Simple
Brisk Auto Detailing
We are mobile (We come to you)
marcus@briskautodetailing.example
briskautodetailing.example
One side should have just the logo with the text underneath and maybe some car design element The other side should have all of the contact information and probably the logo on it too. It should have a classy look to it and be very simple. I also want to say what we specialize in "Hand Wash, Waxing, Paint correction & Interior deep cleaning & More" I'm not really sure exactly how I would like this to look (hence the contest), however just very simple and stylish.
Logo on the back with some design element.

```html
<!DOCTYPE html>
<html lang="en">
<head>
<meta charset="utf-8">
<title>Brisk Auto Detailing – Business Card</title>
<link rel="stylesheet" href="https://fonts.googleapis.com/css2?family=Montserrat:wght@400;600;800&display=swap">
<style>
  :root {
    --backdrop: #27cbbb;
    --card: #0b0b0c;
    --accent: #2fc4e8;
    --ink: #ffffff;
    --muted: #cfd6da;
  }
  html, body {
    margin: 0;
    width: 1200px;
    height: 901px;
    overflow: hidden;
    background: var(--backdrop);
    font-family: "Montserrat", sans-serif;
  }
  .sheet {
    position: relative;
    width: 1200px;
    height: 901px;
    display: flex;
    align-items: center;
    justify-content: center;
    gap: 40px;
  }
  .card {
    position: relative;
    width: 540px;
    height: 309px;
    background: var(--card);
    border-radius: 4px;
    box-shadow: 0 14px 30px rgba(0,0,0,.25);
    overflow: hidden;
    color: var(--ink);
  }
  /* Front */
  .card--front {
    display: flex;
    flex-direction: column;
    align-items: center;
    justify-content: center;
  }
  .wordmark {
    display: flex;
    align-items: center;
    gap: 12px;
    font-weight: 800;
    font-size: 34px;
    letter-spacing: 1px;
    text-transform: uppercase;
    color: var(--ink);
  }
  .wordmark__dot {
    width: 14px;
    height: 14px;
    border-radius: 50%;
    background: var(--ink);
  }
  .front__url {
    margin-top: 12px;
    font-size: 12px;
    letter-spacing: 2px;
    color: var(--accent);
  }
  /* Back */
  .identity {
    position: absolute;
    top: 34px;
    right: 36px;
    text-align: right;
  }
  .identity__name { font-size: 20px; font-weight: 400; margin: 0; }
  .identity__role { font-size: 10px; margin: 3px 0 0; color: var(--muted); }
  .identity__social { font-size: 9px; margin: 14px 0 0; color: var(--muted); }
  .contacts {
    position: absolute;
    top: 124px;
    right: 36px;
    list-style: none;
    margin: 0;
    padding: 0;
    text-align: right;
    font-size: 11px;
    line-height: 17px;
  }
  .contacts li { display: flex; justify-content: flex-end; align-items: center; gap: 8px; }
  .contacts__icon { width: 8px; height: 8px; background: var(--accent); }
  .back__logo {
    position: absolute;
    left: 30px;
    bottom: 52px;
  }
  .back__logo .wordmark { font-size: 22px; color: var(--accent); gap: 8px; }
  .back__logo .wordmark__dot { width: 10px; height: 10px; background: var(--accent); }
  .back__tagline-mobile {
    margin: 4px 0 0;
    font-size: 12px;
    letter-spacing: 3px;
    color: var(--accent);
    text-transform: lowercase;
  }
  .services-band {
    position: absolute;
    left: 0; right: 0; bottom: 0;
    height: 26px;
    background: var(--accent);
    display: flex;
    align-items: center;
    justify-content: center;
    font-size: 10px;
    font-weight: 600;
    color: var(--card);
  }
</style>
</head>
<body>
<main class="sheet">
  <section class="card card--front" aria-label="Card front">
    <div class="wordmark"><span class="wordmark__dot"></span>Brisk Auto Detailing</div>
    <div class="front__url">briskautodetailing.example</div>
  </section>

  <section class="card card--back" aria-label="Card back">
    <div class="identity">
      <p class="identity__name">Marcus Reid</p>
      <p class="identity__role">Managing Director</p>
      <p class="identity__social">Find us on</p>
    </div>
    <ul class="contacts">
      <li>+11 555 010 234 <span class="contacts__icon"></span></li>
      <li>marcus@briskautodetailing.example <span class="contacts__icon"></span></li>
      <li>briskautodetailing.example <span class="contacts__icon"></span></li>
      <li>briskautodetailing.example <span class="contacts__icon"></span></li>
      <li>@briskautodetailing <span class="contacts__icon"></span></li>
    </ul>
    <div class="back__logo">
      <div class="wordmark"><span class="wordmark__dot"></span>Brisk Auto Detailing</div>
      <p class="back__tagline-mobile">We are mobile</p>
    </div>
    <div class="services-band">"Hand Wash, Waxing, Paint correction &amp; Interior deep cleaning &amp; More"</div>
  </section>
</main>
</body>
</html>
```